Brand Design/Redesign

Design and/or redesign an identity for product and organisation
Create visual identity (colours, fonts), website, mobile app, web application, online campaigns, social media.

I have given a sample wireframe for you to use so that we can really get a sense of the colour palette you are choosing and how it will look in a live context.

Considerations when Choosing:
Brand is for Gen Z -
With a particular focus on 16 - 18 years old.

There will be a commercial portal for Business to use also.

Please outline in a short paragraph why you choose the colours and their relationship to our target audience.

Selected winner to produce Brand Identity Document

Please see document attached.

Target Market(s)

Gen Z 16 - 18 yearolds

Industry/Entity Type

Social Media

Requirements
Must have
• Colour Palette & Font Selections, Visual of Colour Palette & Winner to produce Brand Identity Doc
Nice to have
• Really Cool, Edgy and Appeal to aYoung Audience
Should not have
• A corporate feel to it

```html
<!DOCTYPE html>
<html lang="en">
<head>
<meta charset="utf-8">
<title>Home screen – Sunset and Ultraviolet palettes</title>
<link rel="stylesheet" href="https://fonts.googleapis.com/css2?family=Inter:wght@400;500;600;700&display=swap">
<style>
  :root {
    --page-bg: #5f6675;
    --screen-bg: #0f1321;
    --card-bg: #1c2130;
    --card-bg-2: #232838;
    --field-border: #323a4d;
    --text-main: #f2f3f7;
    --text-soft: #c9ccd6;
    --text-muted: #8d93a3;
    --tab-bg: #2a3040;
    --nav-bg: #1a1f2e;
  }
  .theme-sunset {
    --accent-a: #ff3f8e;
    --accent-b: #ffb21c;
    --accent-text: #ff8a3d;
    --glow: rgba(255, 170, 40, 0.35);
    --card-edge: #5d4a2c;
  }
  .theme-ultraviolet {
    --accent-a: #ff3f9c;
    --accent-b: #a63af2;
    --accent-text: #e64fd0;
    --glow: rgba(170, 60, 240, 0.45);
    --card-edge: #4d3a6e;
  }
  * { box-sizing: border-box; margin: 0; padding: 0; }
  html, body {
    width: 1200px; height: 1113px; overflow: hidden;
    background: var(--page-bg);
    font-family: "Inter", Arial, sans-serif;
    letter-spacing: -0.02em;
  }
  .stage { position: relative; width: 1200px; height: 1113px; }
  .screen {
    position: absolute; top: 108px; width: 414px; height: 896px;
    background: var(--screen-bg); border-radius: 44px; overflow: hidden;
    color: var(--text-main);
  }
  .screen--left { left: 120px; }
  .screen--right { left: 663px; }
  .abs { position: absolute; }

  .status-time { left: 20px; top: 11px; font-size: 14px; font-weight: 600; }
  .status-icons { right: 20px; top: 12px; }

  .search {
    left: 16px; top: 55px; width: 383px; height: 46px;
    border: 1px solid var(--field-border); border-radius: 8px;
    display: flex; align-items: center; gap: 10px; padding-left: 16px;
    color: var(--text-muted); font-size: 13.5px;
  }
  .tab {
    top: 129px; height: 35px; border-radius: 18px;
    display: flex; align-items: center; justify-content: center;
    font-size: 13px; font-weight: 500;
  }
  .tab--active {
    left: 16px; width: 102px; color: var(--accent-text);
    border: 1.5px solid transparent;
    background: linear-gradient(var(--screen-bg), var(--screen-bg)) padding-box,
                linear-gradient(90deg, var(--accent-a), var(--accent-b)) border-box;
  }
  .tab--news { left: 134px; width: 94px; background: var(--tab-bg); color: var(--text-main); }

  .challenge {
    left: 16px; top: 181px; width: 383px; height: 215px; border-radius: 10px;
    border: 1px solid var(--card-edge);
    background: radial-gradient(circle at 78% 45%, var(--glow), transparent 55%), var(--card-bg);
  }
  .challenge__title { left: 26px; top: 26px; font-size: 22px; font-weight: 600; }
  .challenge__body { left: 26px; top: 66px; width: 200px; font-size: 12px; line-height: 20.5px; color: var(--text-soft); }
  .challenge__art {
    left: 248px; top: 18px; width: 110px; height: 180px; border-radius: 50% 50% 40% 40%;
    background: radial-gradient(ellipse at 50% 40%, #f4eef4 0 22%, var(--accent-a) 38%, var(--accent-b) 60%, transparent 75%);
    opacity: 0.85;
  }
  .btn {
    border-radius: 4px; display: flex; align-items: center; justify-content: center;
    background: linear-gradient(90deg, var(--accent-a), var(--accent-b));
    color: #1a1420; font-weight: 600;
  }
  .theme-ultraviolet .btn { color: #ffffff; }
  .challenge__cta { left: 26px; top: 149px; width: 139px; height: 39px; font-size: 12.5px; gap: 6px; }

  .greeting, .balance {
    top: 410px; width: 184px; height: 104px; border-radius: 8px; background: var(--card-bg); overflow: hidden;
  }
  .greeting { left: 16px; }
  .greeting__name { left: 17px; top: 17px; font-size: 18px; font-weight: 600; }
  .greeting__bar {
    left: 0; bottom: 0; width: 100%; height: 42px;
    background: linear-gradient(90deg, var(--accent-a), var(--accent-b));
    display: flex; align-items: center; justify-content: space-between; padding: 0 17px 0 18px;
    font-size: 21px; font-weight: 600; color: #ffffff;
  }
  .theme-sunset .greeting__bar { color: #1a1420; }
  .greeting__count { display: flex; align-items: center; gap: 5px; }
  .balance { left: 215px; }
  .balance__amount {
    left: 16px; top: 10px; font-size: 31px; font-weight: 700;
    background: linear-gradient(90deg, var(--accent-a), var(--accent-b));
    -webkit-background-clip: text; background-clip: text; color: transparent;
  }
  .balance__last { left: 16px; top: 62px; font-size: 11px; color: var(--text-soft); }
  .balance__last strong { font-size: 15px; color: var(--text-main); font-weight: 600; margin-left: 3px; }
  .balance__source { left: 16px; top: 84px; font-size: 11px; color: var(--text-soft); }

  .section-title { left: 16px; top: 555px; font-size: 21px; font-weight: 600; }
  .section-more { right: 15px; top: 561px; font-size: 13px; color: var(--accent-text); font-weight: 500; }

  .brand-card, .action-card { top: 591px; width: 184px; border-radius: 8px; background: var(--card-bg-2); }
  .brand-card { left: 16px; height: 167px; }
  .action-card { left: 214px; height: 190px; }
  .avatar {
    width: 43px; height: 43px; border-radius: 50%;
    border: 1.5px solid var(--accent-a); background: #121522;
  }
  .brand-card .avatar { left: 17px; top: 14px; }
  .brand-card__name { left: 75px; top: 15px; font-size: 18px; font-weight: 600; }
  .brand-card__tags { left: 75px; top: 42px; width: 100px; font-size: 11px; line-height: 16px; color: var(--text-soft); word-spacing: 8px; }
  .brand-card__label { left: 17px; top: 90px; font-size: 11px; line-height: 16px; color: var(--text-soft); }
  .brand-card__count { left: 17px; top: 127px; font-size: 19px; font-weight: 600; }
  .brand-card__follow { left: 98px; top: 109px; width: 70px; height: 29px; font-size: 11px; border-radius: 3px; }
  .theme-sunset .brand-card__follow { color: #1a1420; }
  .action-card .avatar { left: 18px; top: 14px; }
  .action-card__org { left: 18px; top: 68px; font-size: 11px; color: var(--text-soft); }
  .action-card__title { left: 18px; top: 98px; width: 150px; font-size: 19px; line-height: 29px; font-weight: 600; }
  .action-card__meta { left: 18px; top: 160px; font-size: 11px; color: var(--text-soft); display: flex; align-items: center; gap: 6px; }

  .tabbar {
    left: 0; top: 822px; width: 414px; height: 74px; background: var(--nav-bg);
    display: flex; justify-content: space-around; padding: 14px 6px 0;
  }
  .tabbar__item { width: 100px; display: flex; flex-direction: column; align-items: center; gap: 4px; font-size: 12px; color: var(--text-muted); }
  .tabbar__item--active { color: var(--accent-text); }
</style>
</head>
<body>
<div class="stage">

<!-- Sunset palette -->
<section class="screen screen--left theme-sunset">
  <span class="abs status-time">9:20</span>
  <svg class="abs status-icons" width="56" height="12" viewBox="0 0 56 12" fill="#e8e9ee">
    <rect x="0" y="7" width="2.5" height="5"/><rect x="4" y="4" width="2.5" height="8"/><rect x="8" y="1" width="2.5" height="11"/>
    <path d="M20 5a9 9 0 0 1 12 0l-1.5 1.6a7 7 0 0 0-9 0zM22.5 7.8a5 5 0 0 1 7 0L26 11.5z"/>
    <rect x="40" y="2.5" width="14" height="8" rx="2"/>
  </svg>
  <div class="abs search">
    <svg width="18" height="18" viewBox="0 0 18 18" fill="none" stroke="#9aa0ae" stroke-width="1.6"><circle cx="7.5" cy="7.5" r="6"/><path d="M12 12l5 5"/></svg>
    Search
  </div>
  <div class="abs tab tab--active">For you</div>
  <div class="abs tab tab--news">News</div>

  <article class="abs challenge">
    <h2 class="abs challenge__title">Daily Challenge</h2>
    <p class="abs challenge__body">But I must explain to you how all mistaken idea of denouncing and praising pain</p>
    <div class="abs challenge__art" role="img" aria-label="Illustration of a rocket taking off"></div>
    <div class="abs btn challenge__cta">Start now <span>&gt;</span></div>
  </article>

  <div class="abs greeting">
    <span class="abs greeting__name">Hi, Charlie</span>
    <div class="abs greeting__bar">
      <span class="greeting__count">8
        <svg width="16" height="18" viewBox="0 0 16 18" fill="none" stroke="currentColor" stroke-width="1.8"><path d="M3 13V8a5 5 0 0 1 10 0v5l1.5 1.5h-13zM6.5 16.5h3"/></svg>
      </span>
      <svg width="20" height="20" viewBox="0 0 20 20" fill="none" stroke="currentColor" stroke-width="1.5"><circle cx="10" cy="10" r="8.5"/><path d="M8.5 6.5L12 10l-3.5 3.5"/></svg>
    </div>
  </div>
  <div class="abs balance">
    <span class="abs balance__amount">$ 543</span>
    <span class="abs balance__last">Last earning: <strong>$120</strong></span>
    <span class="abs balance__source">Lumera adverstiment review</span>
  </div>

  <h3 class="abs section-title">Discover</h3>
  <span class="abs section-more">More</span>

  <article class="abs brand-card">
    <div class="abs avatar"></div>
    <span class="abs brand-card__name">Stridewell</span>
    <p class="abs brand-card__tags">#sport #lifestyle #lifestyle</p>
    <p class="abs brand-card__label">Actions<br>providing</p>
    <span class="abs brand-card__count">233</span>
    <div class="abs btn brand-card__follow">Follow</div>
  </article>
  <article class="abs action-card">
    <div class="abs avatar"></div>
    <span class="abs action-card__org">Aerolune</span>
    <h4 class="abs action-card__title">My first action title</h4>
    <span class="abs action-card__meta">
      <svg width="11" height="11" viewBox="0 0 11 11" fill="none" stroke="#c9ccd6" stroke-width="1"><rect x="0.5" y="1.5" width="10" height="9"/><path d="M0.5 4h10M3 0v3M8 0v3"/></svg>
      05 days remaining
    </span>
  </article>

  <nav class="abs tabbar">
    <div class="tabbar__item tabbar__item--active">
      <svg width="22" height="22" viewBox="0 0 22 22" fill="none" stroke="currentColor" stroke-width="1.6"><path d="M3 9l8-6 8 6v10H3zM9 19v-5h4v5"/></svg>Home</div>
    <div class="tabbar__item">
      <svg width="24" height="22" viewBox="0 0 24 22" fill="none" stroke="currentColor" stroke-width="1.6"><rect x="2" y="6" width="20" height="14" rx="2"/><path d="M8 6V3h8v3"/></svg>Marketplace</div>
    <div class="tabbar__item">
      <svg width="22" height="22" viewBox="0 0 22 22" fill="none" stroke="currentColor" stroke-width="1.6"><rect x="3" y="2" width="16" height="5"/><path d="M4 7v13h14V7M8 11h6"/></svg>Vault</div>
    <div class="tabbar__item">
      <svg width="22" height="22" viewBox="0 0 22 22" fill="none" stroke="currentColor" stroke-width="1.6"><circle cx="11" cy="11" r="9.5"/><circle cx="11" cy="9" r="3"/><path d="M5.5 17a6 6 0 0 1 11 0"/></svg>Profile</div>
  </nav>
</section>

<!-- Ultraviolet palette -->
<section class="screen screen--right theme-ultraviolet">
  <span class="abs status-time">9:20</span>
  <svg class="abs status-icons" width="56" height="12" viewBox="0 0 56 12" fill="#e8e9ee">
    <rect x="0" y="7" width="2.5" height="5"/><rect x="4" y="4" width="2.5" height="8"/><rect x="8" y="1" width="2.5" height="11"/>
    <path d="M20 5a9 9 0 0 1 12 0l-1.5 1.6a7 7 0 0 0-9 0zM22.5 7.8a5 5 0 0 1 7 0L26 11.5z"/>
    <rect x="40" y="2.5" width="14" height="8" rx="2"/>
  </svg>
  <div class="abs search">
    <svg width="18" height="18" viewBox="0 0 18 18" fill="none" stroke="#9aa0ae" stroke-width="1.6"><circle cx="7.5" cy="7.5" r="6"/><path d="M12 12l5 5"/></svg>
    Search
  </div>
  <div class="abs tab tab--active">For you</div>
  <div class="abs tab tab--news">News</div>

  <article class="abs challenge">
    <h2 class="abs challenge__title">Daily Challenge</h2>
    <p class="abs challenge__body">But I must explain to you how all mistaken idea of denouncing and praising pain</p>
    <div class="abs challenge__art" role="img" aria-label="Illustration of a rocket taking off"></div>
    <div class="abs btn challenge__cta">Start now <span>&gt;</span></div>
  </article>

  <div class="abs greeting">
    <span class="abs greeting__name">Hi, Charlie</span>
    <div class="abs greeting__bar">
      <span class="greeting__count">8
        <svg width="16" height="18" viewBox="0 0 16 18" fill="none" stroke="currentColor" stroke-width="1.8"><path d="M3 13V8a5 5 0 0 1 10 0v5l1.5 1.5h-13zM6.5 16.5h3"/></svg>
      </span>
      <svg width="20" height="20" viewBox="0 0 20 20" fill="none" stroke="currentColor" stroke-width="1.5"><circle cx="10" cy="10" r="8.5"/><path d="M8.5 6.5L12 10l-3.5 3.5"/></svg>
    </div>
  </div>
  <div class="abs balance">
    <span class="abs balance__amount">$ 543</span>
    <span class="abs balance__last">Last earning: <strong>$120</strong></span>
    <span class="abs balance__source">Lumera adverstiment review</span>
  </div>

  <h3 class="abs section-title">Discover</h3>
  <span class="abs section-more">More</span>

  <article class="abs brand-card">
    <div class="abs avatar"></div>
    <span class="abs brand-card__name">Stridewell</span>
    <p class="abs brand-card__tags">#sport #lifestyle #lifestyle</p>
    <p class="abs brand-card__label">Actions<br>providing</p>
    <span class="abs brand-card__count">233</span>
    <div class="abs btn brand-card__follow">Follow</div>
  </article>
  <article class="abs action-card">
    <div class="abs avatar"></div>
    <span class="abs action-card__org">Aerolune</span>
    <h4 class="abs action-card__title">My first action title</h4>
    <span class="abs action-card__meta">
      <svg width="11" height="11" viewBox="0 0 11 11" fill="none" stroke="#c9ccd6" stroke-width="1"><rect x="0.5" y="1.5" width="10" height="9"/><path d="M0.5 4h10M3 0v3M8 0v3"/></svg>
      05 days remaining
    </span>
  </article>

  <nav class="abs tabbar">
    <div class="tabbar__item tabbar__item--active">
      <svg width="22" height="22" viewBox="0 0 22 22" fill="none" stroke="currentColor" stroke-width="1.6"><path d="M3 9l8-6 8 6v10H3zM9 19v-5h4v5"/></svg>Home</div>
    <div class="tabbar__item">
      <svg width="24" height="22" viewBox="0 0 24 22" fill="none" stroke="currentColor" stroke-width="1.6"><rect x="2" y="6" width="20" height="14" rx="2"/><path d="M8 6V3h8v3"/></svg>Marketplace</div>
    <div class="tabbar__item">
      <svg width="22" height="22" viewBox="0 0 22 22" fill="none" stroke="currentColor" stroke-width="1.6"><rect x="3" y="2" width="16" height="5"/><path d="M4 7v13h14V7M8 11h6"/></svg>Vault</div>
    <div class="tabbar__item">
      <svg width="22" height="22" viewBox="0 0 22 22" fill="none" stroke="currentColor" stroke-width="1.6"><circle cx="11" cy="11" r="9.5"/><circle cx="11" cy="9" r="3"/><path d="M5.5 17a6 6 0 0 1 11 0"/></svg>Profile</div>
  </nav>
</section>

</div>
</body>
</html>
```